Redesign of a facility management homepage

We need a redesign/an improved design of the facility management homepage (http://www.krt-lanzfeld.de/).
This websites offers detailed information on the "About us" as company, the "Services" provided and special information on facility and strata management. We would like to keep the structure of the website.
We need ideas/designs how this website could look more modern and confidential and appealing/pleasant for visitors at the same time and not losing the main purpose of information distribution.
The green color must be used since this is the basic color from our logo.
The blue in the background of the logo ist optional. So feel to use it or not.
We need no coding only design (.psd or as .ai)

```html
<!DOCTYPE html>
<html lang="en">
<head>
<meta charset="utf-8">
<title>KRT Office and Janitorial Service GmbH</title>
<link href="https://fonts.googleapis.com/css2?family=Open+Sans:wght@300;400;600&family=Cabin:wght@400;500;600&display=swap" rel="stylesheet">
<style>
:root{
  --green:#2d8a22;
  --green-dark:#1f6e17;
  --green-soft:#7fbf6a;
  --nav:#3a3a3a;
  --text:#555;
  --heading:#2d8a22;
  --rule:#c9c9c9;
  --icon:#6a6a6a;
  --side:#cfcfcf;
}
*{box-sizing:border-box;margin:0;padding:0}
html,body{width:1093px;height:1200px;overflow:hidden}
body{background:linear-gradient(90deg,#c4c4c4,#dcdcdc 6%,#dcdcdc 94%,#c4c4c4);font-family:"Open Sans",sans-serif;color:var(--text);position:relative}
.page{position:absolute;left:68px;top:0;width:959px;height:1200px;background:#fff}
.abs{position:absolute}

/* header */
.brand{left:137px;top:23px;display:flex;align-items:center;gap:10px}
.brand-mark{width:40px;height:40px;background:var(--green)}
.brand-name{font-family:"Cabin",sans-serif;font-weight:600;font-size:34px;color:var(--green);letter-spacing:1px}
.brand-divider{left:258px;top:53px;width:2px;height:43px;background:var(--green)}
.tagline{left:270px;top:59px;font-family:"Cabin",sans-serif;font-weight:500;font-size:13px;line-height:18px;color:var(--green);letter-spacing:.3px}
.social{left:761px;top:63px;display:flex;gap:7px}
.social span{width:27px;height:27px;border-radius:50%;background:var(--icon);display:block}
.contact{right:145px;top:100px;font-size:11px;color:#777;display:flex;gap:14px;align-items:center}
.contact svg{vertical-align:-2px;margin-left:4px}

/* nav */
.nav{left:128px;top:125px;width:835px;height:39px;background:var(--nav);display:flex;align-items:center;box-shadow:0 2px 3px rgba(0,0,0,.3)}
.nav a{color:#fff;text-decoration:none;font-size:11.5px;height:39px;display:flex;align-items:center;padding:0 10px;border-right:1px solid #555}
.nav a.home{background:var(--green);width:118px;justify-content:center}
.nav a.w1{width:91px;justify-content:center}
.nav a.w2{width:134px;justify-content:center}
.nav a.w3{width:135px;justify-content:center}
.nav a.w4{width:73px;justify-content:center}
.nav a.w5{width:82px;justify-content:center;border-right:none}
.search{position:absolute;left:659px;top:6px;width:160px;height:26px;background:#fff;font-size:9px;color:#888;padding:7px 8px}
.search svg{position:absolute;right:8px;top:8px}

/* hero */
.hero{left:137px;top:164px;width:818px;height:328px;border-radius:0 0 8px 8px;background:linear-gradient(180deg,#c9a46a 0%,#e2d6b8 30%,#d9dadb 55%,#8d8a83 80%,#6e6b66 100%);box-shadow:0 3px 5px rgba(0,0,0,.25);overflow:hidden}
.hero-card{left:635px;top:326px;width:320px;height:119px;background:rgba(34,128,26,.93);border-radius:3px 0 0 3px;padding:10px 22px;color:#fff}
.hero-card h1{font-family:"Cabin",sans-serif;font-weight:500;font-size:41px;letter-spacing:1px;line-height:42px}
.hero-card p{font-size:10.3px;line-height:15.5px;margin-top:4px}
.hero-card em{color:#f4e04a}

/* sections */
.section-title{font-family:"Open Sans",sans-serif;font-size:15.5px;color:var(--heading);display:flex;align-items:center;gap:14px}
.section-title::after{content:"";flex:1;height:1px;background:var(--rule)}
.body-copy{font-size:10.3px;line-height:17.5px;color:var(--text)}
.more{color:var(--green);font-style:italic}
.arrows{display:flex;gap:5px}
.arrows span{width:13px;height:13px;border-radius:50%;background:#2b2b2b;display:flex;align-items:center;justify-content:center}

.about-title{left:142px;top:527px;width:379px}
.about-copy{left:139px;top:553px;width:388px}
.about-copy p+p{margin-top:8px}

.service-title{left:566px;top:526px;width:386px}
.service-arrows{left:912px;top:515px}
.service{width:183px}
.service .photo{height:87px;border-bottom:3px solid var(--green)}
.service h3{font-weight:400;font-size:13px;color:#333;padding:10px 4px 5px;border-bottom:1px solid var(--rule);margin-bottom:6px}
.service p{font-size:10.3px;line-height:14px;padding-left:3px}
.photo-vans{background:linear-gradient(180deg,#c9a46a,#e8e6e2 50%,#7d7a74)}
.photo-house{background:linear-gradient(180deg,#c9a189,#dbb19a 45%,#b84a3a 70%,#9a7f70)}

.news-title{left:145px;top:754px;width:373px}
.news-arrows{left:487px;top:744px}
.news{width:180px}
.date{position:absolute;left:0;top:0;width:33px}
.date b{display:block;height:33px;background:#f1f1f1;color:#999;font-weight:400;font-size:13px;text-align:center;line-height:33px}
.date i{display:block;height:18px;background:var(--green);color:#fff;font-style:normal;font-size:12.5px;text-align:center;line-height:18px}
.news h4{margin-left:49px;font-weight:400;font-size:11.5px;line-height:17px;color:#333}
.news p{margin-left:49px;margin-top:9px;font-size:10.3px;line-height:17px;color:#777}

.testi-title{left:569px;top:752px;font-size:13px;color:#222;font-weight:600}
.testi-title span{font-weight:300;color:#999}
.quote{left:569px;top:793px;width:369px;height:88px;background:var(--green-soft);padding:17px 30px;font-size:10.2px;line-height:17.5px;color:#1d2a18}
.quote-tail{left:590px;top:881px}
.quote-by{right:155px;top:888px;font-size:10.3px;color:#999}
.quote-by b{font-weight:400;color:#8aa637}

.dotted{left:148px;top:932px;width:736px;border-top:2px dotted #d0d0d0}
.promo-arrows{left:897px;top:926px}
.promo{width:237px;height:152px}
.promo .photo{height:104px}
.promo .label{height:47px;margin-top:1px;background:linear-gradient(180deg,#3a9a2c,#1f7417);border-radius:0 0 4px 4px;color:#fff;font-size:15.5px;letter-spacing:1px;text-align:center;display:flex;align-items:center;justify-content:center;line-height:17px}
.photo-team{background:linear-gradient(135deg,#e8ede8,#d8b89c 50%,#a88870)}
.photo-keys{background:linear-gradient(180deg,#d4d5d7,#9ea1a6 60%,#6f6c6c)}

.footer-rule{left:144px;top:1151px;width:796px;height:1px;background:#ccc}
.footer{left:147px;top:1160px;font-size:10.3px;color:#555;letter-spacing:.5px}
</style>
</head>
<body>
<div class="page"></div>

<header>
  <div class="abs brand"><span class="brand-mark"></span><span class="brand-name">KRT</span></div>
  <div class="abs brand-divider"></div>
  <div class="abs tagline">OFFICE AND JANITORIAL SERVICE GMBH<br>LANZFELD YOUR LOCAL PARTNER</div>
  <div class="abs social" aria-label="Social links"><span></span><span></span><span></span><span></span><span></span><span></span></div>
  <div class="abs contact">
    <span>info@krt-lanzfeld.de<svg width="12" height="9" viewBox="0 0 12 9"><rect x=".5" y=".5" width="11" height="8" fill="none" stroke="#888"/><path d="M.5 .5 6 5 11.5 .5" fill="none" stroke="#888"/></svg></span>
    <span><svg width="7" height="11" viewBox="0 0 7 11"><rect x=".5" y=".5" width="6" height="10" rx="1" fill="none" stroke="#888"/><rect x="2.5" y="8" width="2" height="1" fill="#888"/></svg> + 356 555 0142</span>
  </div>
  <nav class="abs nav">
    <a class="home" href="#">Home</a>
    <a class="w1" href="#">About Us</a>
    <a class="w2" href="#">Building Management</a>
    <a class="w3" href="#">Building Management</a>
    <a class="w4" href="#">Rentals</a>
    <a class="w5" href="#">Contact Us</a>
    <div class="search">Search<svg width="10" height="10" viewBox="0 0 10 10"><circle cx="4" cy="4" r="3" fill="none" stroke="#aaa" stroke-width="1.3"/><path d="M6.2 6.2 9 9" stroke="#aaa" stroke-width="1.5"/></svg></div>
  </nav>
</header>

<section class="abs hero" role="img" aria-label="Photo of white company vans parked in front of a building"></section>
<div class="abs hero-card">
  <h1>CAR RENTALS</h1>
  <p>The KRT is an established, experienced and successful services company with lines of business building management <em>read more...</em></p>
</div>

<h2 class="abs section-title about-title">About Us</h2>
<div class="abs about-copy body-copy">
  <p>The KRT is an established, experienced and successful services company with lines of business building management (building management, operating expense reports, etc.), concierge service, winter maintenance, building services, secretarial services, etc.</p>
  <p>The KRT has the latest computer programs and trained, highly experienced and motivated staff.The KRT ensures comprehensive care and ensures preservation of value of the contract objects.The KRT ensures comprehensive care and ensures preservation of value of the contract objects.The KRT ensures comprehensive care and ensures preservation <span class="more">read more...</span></p>
</div>

<h2 class="abs section-title service-title">Our Service</h2>
<div class="abs arrows service-arrows"><span><svg width="5" height="7"><path d="M4 0 1 3.5 4 7" fill="none" stroke="#fff" stroke-width="1.5"/></svg></span><span><svg width="5" height="7"><path d="M1 0 4 3.5 1 7" fill="none" stroke="#fff" stroke-width="1.5"/></svg></span></div>
<article class="abs service" style="left:566px;top:555px">
  <div class="photo photo-vans" role="img" aria-label="Photo of company vans"></div>
  <h3>Car Rental</h3>
  <p>The KRT has the latest computer programs and trained, highly experienced <span class="more">read more...</span></p>
</article>
<article class="abs service" style="left:768px;top:555px">
  <div class="photo photo-house" role="img" aria-label="Photo of hands sheltering a small model house"></div>
  <h3>Building Management</h3>
  <p>The KRT has the latest computer programs and trained, highly experienced <span class="more">read more...</span></p>
</article>

<h2 class="abs section-title news-title">Recent News</h2>
<div class="abs arrows news-arrows"><span><svg width="5" height="7"><path d="M4 0 1 3.5 4 7" fill="none" stroke="#fff" stroke-width="1.5"/></svg></span><span><svg width="5" height="7"><path d="M1 0 4 3.5 1 7" fill="none" stroke="#fff" stroke-width="1.5"/></svg></span></div>
<article class="abs news" style="left:150px;top:785px">
  <div class="date"><b>28</b><i>Dec</i></div>
  <h4>The Boating Life Begins With a Good Storm</h4>
  <p>Integer libero lectus, porta acean pulvinar ac, facilisis non arcu. Maecenas enim</p>
</article>
<article class="abs news" style="left:343px;top:785px">
  <div class="date"><b>15</b><i>Dec</i></div>
  <h4>Visiting Tuscany Without the Crowds</h4>
  <p>Integer libero lectus, porta acean pulvinar ac, facilisis non arcu. Maecenas enim</p>
</article>

<h2 class="abs testi-title">Testimonials <span>/ What Our Clients Say</span></h2>
<blockquote class="abs quote">The KRT is an established, experienced and successful services company with lines of business building management (building management, operating expense reports...</blockquote>
<svg class="abs quote-tail" width="12" height="13" viewBox="0 0 12 13"><path d="M0 0H12L12 13Z" fill="#7fbf6a"/></svg>
<div class="abs quote-by"><b>Martin</b>, Project Manager</div>

<div class="abs dotted"></div>
<div class="abs arrows promo-arrows"><span><svg width="5" height="7"><path d="M4 0 1 3.5 4 7" fill="none" stroke="#fff" stroke-width="1.5"/></svg></span><span><svg width="5" height="7"><path d="M1 0 4 3.5 1 7" fill="none" stroke="#fff" stroke-width="1.5"/></svg></span></div>
<a class="abs promo" style="left:143px;top:957px">
  <div class="photo photo-team" role="img" aria-label="Photo of a customer service team with headsets"></div>
  <div class="label">REPORT<br>DISORDER ONLINE</div>
</a>
<a class="abs promo" style="left:422px;top:957px">
  <div class="photo photo-keys" role="img" aria-label="Photo of hands typing on a keyboard"></div>
  <div class="label">ON THE LEFT</div>
</a>
<a class="abs promo" style="left:697px;top:957px">
  <div class="photo photo-house" role="img" aria-label="Photo of hands sheltering a small model house"></div>
  <div class="label">IMPRINT</div>
</a>

<div class="abs footer-rule"></div>
<footer class="abs footer">© 2014 KRT.All Rights Reserved</footer>
</body>
</html>
```